Brixel Consulting Limited

we are a company specialising in assisting New Zealand companies to venture into China on strategy, business development, M&A, and Governance.

Industry/Entity Type

Graphic Design

```html
<!DOCTYPE html>
<html lang="en">
<head>
<meta charset="utf-8">
<title>Brixel Consulting Limited – Business Card</title>
<link rel="stylesheet" href="https://fonts.googleapis.com/css2?family=Open+Sans:wght@600;700&family=Quicksand:wght@500;600&display=swap">
<style>
  :root {
    --backdrop: #dadada;
    --card: #ffffff;
    --brand-red: #e8141b;
    --ink: #111111;
    --handset: #b3161c;
    --deco-pink: #fbd5d6;
    --deco-grey: #e3e3e3;
    --chat-blue: #2aa3e0;
  }
  * { margin: 0; padding: 0; box-sizing: border-box; }
  html, body { width: 1200px; height: 1000px; overflow: hidden; }
  body { background: var(--backdrop); position: relative; font-family: "Open Sans", Arial, sans-serif; color: var(--ink); }

  .card {
    position: absolute; width: 717px; height: 400px;
    background: var(--card);
    box-shadow: 4px 4px 5px rgba(0,0,0,0.45);
    overflow: hidden;
  }
  .card--front { left: 63px; top: 41px; }
  .card--back { left: 415px; top: 513px; }

  .deco-square { position: absolute; width: 175px; height: 175px; background: var(--deco-pink); }
  .deco-square--front { left: 447px; top: 100px; }
  .deco-square--back { left: 440px; top: 82px; }
  .deco-bar { position: absolute; background: var(--deco-grey); }
  .deco-bar--front { left: 595px; top: 195px; width: 85px; height: 105px; }
  .deco-bar--back { left: 595px; top: 195px; width: 85px; height: 105px; }

  .brand-square { position: absolute; left: 44px; top: 52px; width: 80px; height: 80px; background: var(--brand-red); }
  .brand-name {
    position: absolute; left: 132px; top: 56px;
    font-family: "Quicksand", Arial, sans-serif; font-weight: 600;
    font-size: 30px; color: var(--brand-red); letter-spacing: 0.5px; white-space: nowrap;
  }
  .services {
    position: absolute; left: 133px; top: 106px;
    font-weight: 700; font-size: 13.5px; white-space: nowrap; word-spacing: 1px;
  }
  .services span { margin-right: 18px; }

  .person { position: absolute; right: 38px; top: 234px; text-align: right; }
  .person__name {
    font-family: "Quicksand", Arial, sans-serif; font-weight: 600;
    font-size: 27px; color: var(--brand-red); letter-spacing: 0.5px; line-height: 1.1;
  }
  .person__title { font-weight: 700; font-size: 16px; margin-right: 22px; margin-top: 2px; }

  .contact-row { position: absolute; display: flex; align-items: center; white-space: nowrap; font-weight: 700; }
  .handset { width: 54px; height: 62px; flex: none; }
  .contact-row--front-phone { left: 44px; top: 298px; font-size: 20px; }
  .contact-row--front-phone .handset { margin-right: 12px; }

  .contact-row--chat { left: 112px; top: 114px; font-size: 25px; }
  .chat-label {
    display: flex; align-items: center; margin-right: 16px;
    font-weight: 700; font-size: 22px; color: var(--chat-blue);
  }
  .chat-label::before {
    content: ""; width: 26px; height: 26px; border-radius: 50%;
    background: var(--chat-blue); margin-right: 8px;
  }
  .contact-row--email { left: 82px; top: 198px; font-size: 24px; }
  .at-sign { color: var(--brand-red); font-size: 44px; margin-right: 10px; line-height: 1; font-weight: 600; }
  .contact-row--back-phone { left: 208px; top: 240px; font-size: 20px; }
  .contact-row--back-phone .handset { margin-right: 14px; }
</style>
</head>
<body>
  <section class="card card--front" aria-label="Business card front">
    <div class="deco-square deco-square--front"></div>
    <div class="deco-bar deco-bar--front"></div>
    <div class="brand-square"></div>
    <h1 class="brand-name">BRIXEL CONSULTING LIMITED</h1>
    <p class="services"><span>BUSINESS DEVELOPMENT</span><span>M &amp; A</span><span>GOVERNANCE</span>STRATEGY</p>
    <div class="person">
      <p class="person__name">MARA TENHOVE</p>
      <p class="person__title">MANAGING DIRECTOR</p>
    </div>
    <p class="contact-row contact-row--front-phone">
      <svg class="handset" viewBox="0 0 54 62" aria-hidden="true">
        <ellipse cx="27" cy="58" rx="22" ry="2.5" fill="#999" opacity="0.6"/>
        <path d="M8 4 L16 2 L22 14 L17 19 Q22 31 33 40 L38 35 L49 42 L46 50 Q40 55 32 50 Q14 37 7 18 Q5 10 8 4 Z" fill="var(--handset)"/>
        <path d="M44 50 q2 6 6 5" stroke="var(--handset)" stroke-width="1.5" fill="none"/>
      </svg>
      +64 21 555 0147
    </p>
  </section>

  <section class="card card--back" aria-label="Business card back">
    <div class="deco-square deco-square--back"></div>
    <div class="deco-bar deco-bar--back"></div>
    <p class="contact-row contact-row--chat"><span class="chat-label">Chatline</span>BRIXELCONSULTING</p>
    <p class="contact-row contact-row--email"><span class="at-sign">@</span>MARA.TENHOVE@BRIXELCONSULTING.COM</p>
    <p class="contact-row contact-row--back-phone">
      <svg class="handset" viewBox="0 0 54 62" aria-hidden="true">
        <ellipse cx="27" cy="58" rx="22" ry="2.5" fill="#999" opacity="0.6"/>
        <path d="M8 4 L16 2 L22 14 L17 19 Q22 31 33 40 L38 35 L49 42 L46 50 Q40 55 32 50 Q14 37 7 18 Q5 10 8 4 Z" fill="var(--handset)"/>
        <path d="M44 50 q2 6 6 5" stroke="var(--handset)" stroke-width="1.5" fill="none"/>
      </svg>
      +64 21 555 0147
    </p>
  </section>
</body>
</html>
```